Interior Decorating and Event Styling Business Card Design

We need a business card design for a bespoke interior decorating and event styling business, mostly weddings. We also do custom paint finishes and painted floor finishes. We want something simple, organic and stylish with good colour tones used.

On our card we would like our services listed like so -

Interior Decorating
Wedding and Event Styling
Bespoke furniture paint finishes
Painted floor finishes

Industry/Entity Type

Paint

Contact Information for Business Card

Mara & Wren Design
Rosalind 0438175264
Tessa 0429357718
rosalind.partow@mailbay.com.au
tessaorkin@mwk7.com.au

```html
<!DOCTYPE html>
<html lang="en">
<head>
<meta charset="utf-8">
<title>Mara &amp; Wren Design – Business Card</title>
<link rel="stylesheet" href="https://fonts.googleapis.com/css2?family=Poiret+One&family=Open+Sans:wght@400&family=Mulish:wght@400;700&display=swap">
<style>
  :root {
    --page: #ffffff;
    --sage-light: #c8d5a3;
    --sage-mid: #b1c08d;
    --sage-edge: #9aab78;
    --ink: #2e2e2c;
    --leaf-dark: #3d4237;
    --leaf-mid: #6f7c58;
    --leaf-light: #98a67c;
  }
  * { margin: 0; padding: 0; box-sizing: border-box; }
  html, body { width: 1004px; height: 1200px; overflow: hidden; background: var(--page); }
  .canvas { position: relative; width: 1004px; height: 1200px; }

  .card {
    position: absolute;
    width: 798px; height: 461px;
    overflow: hidden;
    background: radial-gradient(ellipse at 40% 45%, var(--sage-light) 0%, var(--sage-mid) 55%, var(--sage-edge) 100%);
    color: var(--ink);
  }
  .card--front { left: 103px; top: 84px; }
  .card--back  { left: 106px; top: 633px; }

  .card__art { position: absolute; inset: 0; width: 798px; height: 461px; }

  .brand-name {
    position: absolute; left: 31px; top: 150px;
    font-family: "Poiret One", sans-serif;
    font-size: 47px; font-weight: 400; letter-spacing: 0.5px;
    white-space: nowrap;
  }
  .services {
    position: absolute; left: 62px; top: 245px;
    list-style: none;
    font-family: "Open Sans", sans-serif;
    font-size: 23px;
  }
  .services li { position: relative; padding-left: 27px; height: 48.5px; line-height: 32px; }
  .services li::before {
    content: ""; position: absolute; left: 0; top: 12px;
    width: 9px; height: 9px; border-radius: 50%; background: #5b5e55;
  }

  .contacts {
    position: absolute; left: 387px; top: 122px; width: 340px;
    text-align: center;
    font-family: "Mulish", sans-serif;
  }
  .contact + .contact { margin-top: 38px; }
  .contact__name { font-weight: 700; font-size: 21px; line-height: 30px; }
  .contact--second .contact__name { font-size: 25px; }
  .contact__line { font-size: 23px; line-height: 36px; display: flex; align-items: center; justify-content: center; gap: 6px; }
  .contact__line--email { font-size: 20px; gap: 10px; }
  .icon { width: 20px; height: 20px; fill: none; stroke: var(--ink); stroke-width: 2; }
  .icon--phone { fill: var(--ink); stroke: none; }
</style>
</head>
<body>
<main class="canvas">

  <section class="card card--front">
    <svg class="card__art" viewBox="0 0 798 461" aria-hidden="false">
      <defs>
        <linearGradient id="leaf-tone" x1="0" y1="0" x2="1" y2="1">
          <stop offset="0" stop-color="#7d8a62"/>
          <stop offset="0.5" stop-color="#5f6a4b"/>
          <stop offset="1" stop-color="#8d9b72"/>
        </linearGradient>
      </defs>
      <path role="img" aria-label="Hand-drawn sage leaf and petal pattern, top left corner"
            d="M0 0 L330 0 C322 58 282 98 205 104 C125 110 45 100 0 82 Z"
            fill="url(#leaf-tone)" stroke="#3d4237" stroke-width="3"/>
      <path role="img" aria-label="Large hand-drawn sage leaf and petal cluster along the right edge"
            d="M505 0 C468 80 458 200 478 300 C498 385 560 440 638 461 L798 461 L798 0 Z"
            fill="url(#leaf-tone)" stroke="#3d4237" stroke-width="3"/>
    </svg>
    <h1 class="brand-name">Mara &amp; Wren Design</h1>
    <ul class="services">
      <li>Interior Decorating</li>
      <li>Wedding and Event Styling</li>
      <li>Bespoke furniture paint finishes</li>
      <li>Painted floor finishes</li>
    </ul>
  </section>

  <section class="card card--back">
    <svg class="card__art" viewBox="0 0 798 461">
      <defs>
        <linearGradient id="leaf-tone-back" x1="0" y1="0" x2="1" y2="1">
          <stop offset="0" stop-color="#7d8a62"/>
          <stop offset="0.5" stop-color="#5f6a4b"/>
          <stop offset="1" stop-color="#8d9b72"/>
        </linearGradient>
      </defs>
      <path role="img" aria-label="Large hand-drawn sage leaf and petal cluster along the left edge"
            d="M0 0 L282 0 C320 80 326 180 320 262 C314 342 280 420 222 461 L0 461 Z"
            fill="url(#leaf-tone-back)" stroke="#3d4237" stroke-width="3"/>
      <path role="img" aria-label="Hand-drawn sage leaf and petal pattern, top right corner"
            d="M466 0 L798 0 L798 120 C720 126 622 112 560 90 C510 70 476 40 466 0 Z"
            fill="url(#leaf-tone-back)" stroke="#3d4237" stroke-width="3"/>
    </svg>

    <div class="contacts">
      <div class="contact contact--first">
        <p class="contact__name">Tessa</p>
        <p class="contact__line">
          <svg class="icon icon--phone" viewBox="0 0 24 24"><path d="M6.6 2.5c.6-.4 1.4-.3 1.8.3l2.2 3.3c.4.6.3 1.3-.2 1.8l-1.6 1.4c.9 2.2 2.7 4.3 4.9 5.6l1.5-1.5c.5-.5 1.3-.5 1.8-.1l3.2 2.4c.6.5.7 1.3.2 1.9l-1.6 2c-.6.7-1.6 1-2.5.7C9.9 18.2 5.3 13.2 3.8 6.9c-.2-.9.1-1.8.8-2.4z"/></svg>
          0429357718
        </p>
        <p class="contact__line contact__line--email">
          <svg class="icon" viewBox="0 0 24 24"><rect x="2" y="5" width="20" height="14"/><path d="M2 5l10 8 10-8"/></svg>
          tessaorkin@mwk7.com.au
        </p>
      </div>
      <div class="contact contact--second">
        <p class="contact__name">Rosalind</p>
        <p class="contact__line">
          <svg class="icon icon--phone" viewBox="0 0 24 24"><path d="M6.6 2.5c.6-.4 1.4-.3 1.8.3l2.2 3.3c.4.6.3 1.3-.2 1.8l-1.6 1.4c.9 2.2 2.7 4.3 4.9 5.6l1.5-1.5c.5-.5 1.3-.5 1.8-.1l3.2 2.4c.6.5.7 1.3.2 1.9l-1.6 2c-.6.7-1.6 1-2.5.7C9.9 18.2 5.3 13.2 3.8 6.9c-.2-.9.1-1.8.8-2.4z"/></svg>
          0438175264
        </p>
        <p class="contact__line contact__line--email">
          <svg class="icon" viewBox="0 0 24 24"><rect x="2" y="5" width="20" height="14"/><path d="M2 5l10 8 10-8"/></svg>
          rosalind.partow@mailbay.com.au
        </p>
      </div>
    </div>
  </section>

</main>
</body>
</html>
```